Texas Marsh Reed Conservation League

We need to design the home page of this new website. We would like a fun website design for provides as a resource for members and information for potential members.
Please design so that we can see a portion of background on each side on the website.
I just need the final design files psd no coding needed.
Attached is their logo (colors are not 100% set in stone either so can mess with those as I did in the quick mockup attached)
Attached is a pdf newsletter they send out, you can get a feel for them and what they are about. The design is crappy and we are here to fix that going forward and we are starting with the website.
Here are some quick example websites (design style is open)
- I attached a quick mockup i did just for a content visual but by all means do what you want.
- http://www.lonestarbizladies.org/
- http://www.wqrtf.org/
- http://demo.webkitpalette.com/demo.php?cat=html5themes&host=layoutbazaar&temp=veltrona
- http://www.fieldkeep.org/
- http://www.urbanpantry.org/
- http://www.projectcozy.org/
here are some of the other chapters website (pretty bad!)
and here are some of the others:
- http://www.kdwrcl.org/
- http://wrcl.org/
- http://www.gwrcl.org/
Content Items that need to be included:
1. Logo
2. Menu - home, about, members, resources, events, membership, contact
3. Become a member - button or action
4. social links - facebook, linkedin, youtube
5. banner - that needs to explain their purpose "Promoting environmental stewardship through operations, research, education and outreach" (or this can be worked into the design)
6. Upcoming event (s)
7. Advertisement - members can place an ad on the website, this can be a placeholder for now
8. newsletter signup
9. advertise with us - this link can be in the footer
30-60 years of age, succesfull (household budgets of 120K+ men and women that live in texas.
Education

```html
<!DOCTYPE html>
<html lang="en">
<head>
<meta charset="utf-8">
<title>Texas Marsh Reed Conservation League</title>
<link rel="stylesheet" href="https://fonts.googleapis.com/css2?family=Open+Sans:wght@400;600;700&family=Tinos:wght@400&display=swap">
<style>
  :root {
    --navy: #0e2262;
    --maroon: #6b1a2c;
    --wine: #9a2a46;
    --yellow: #f4f10a;
    --paper: #f3f3f2;
    --footer: #e7eaed;
    --ink: #222;
    --muted: #777;
    --bar: #2e2f31;
    --white: #fff;
  }
  * { box-sizing: border-box; margin: 0; padding: 0; }
  html, body { width: 820px; height: 1200px; overflow: hidden; }
  body { position: relative; font-family: "Open Sans", sans-serif; color: var(--ink); background: var(--paper); }

  .site-header { position: absolute; left: 0; top: 0; width: 820px; height: 72px; background: rgba(255,255,255,.82); z-index: 3; border-bottom: 4px solid rgba(255,255,255,.9); }
  .brand { position: absolute; left: 125px; top: 0; width: 186px; height: 94px; background: var(--white); border: 1px solid #ccc; display: flex; align-items: center; gap: 8px; padding: 0 12px; }
  .brand-mark { width: 14px; height: 14px; background: var(--navy); flex: none; }
  .brand-name { font-size: 12px; font-weight: 700; line-height: 1.25; color: var(--navy); text-transform: uppercase; }
  .main-nav { position: absolute; left: 370px; top: 0; display: flex; height: 72px; }
  .main-nav a { font-size: 10px; color: #333; text-decoration: none; padding: 0 9px; line-height: 72px; }
  .main-nav a.is-active { background: var(--maroon); color: var(--white); padding: 0 8px; }

  .hero { position: absolute; left: 0; top: 0; width: 820px; height: 367px; background: linear-gradient(160deg, #8c9a52 0%, #b9b477 30%, #6f8a3e 55%, #c7c08a 75%, #53702e 100%); }
  .hero-title { position: absolute; top: 140px; width: 100%; text-align: center; font-weight: 600; font-size: 42px; line-height: 48px; color: var(--white); }
  .hero-title .accent { color: var(--yellow); }
  .slider-dots { position: absolute; left: 580px; top: 348px; display: flex; gap: 8px; }
  .slider-dots span { width: 38px; height: 4px; background: var(--white); }
  .slider-dots span:first-child { background: var(--navy); }

  .join-band { position: absolute; left: 0; top: 367px; width: 820px; height: 69px; background: var(--navy); color: var(--white); }
  .join-band h2 { position: absolute; left: 118px; top: 13px; font-size: 20px; font-weight: 700; letter-spacing: .2px; }
  .join-band p { position: absolute; left: 118px; top: 40px; font-size: 14px; text-transform: uppercase; }
  .join-button { position: absolute; left: 553px; top: 17px; width: 142px; height: 37px; border: 2px solid var(--white); display: flex; align-items: center; gap: 8px; padding-left: 6px; color: var(--white); text-decoration: none; font-size: 14px; line-height: 15px; }
  .join-button b { font-weight: 700; }

  .features { position: absolute; left: 110px; top: 455px; width: 600px; display: flex; justify-content: space-between; }
  .feature { width: 150px; text-align: center; }
  .feature-icon { width: 60px; height: 60px; margin: 0 auto 20px; background: #d6d6d4; border-radius: 50%; }
  .feature h3 { font-size: 9px; font-weight: 700; margin-bottom: 10px; }
  .feature p { font-size: 7.5px; color: var(--muted); line-height: 10px; }

  .newsletter { position: absolute; left: 110px; top: 622px; width: 600px; height: 70px; background: var(--wine); color: var(--white); }
  .newsletter h2 { position: absolute; left: 11px; top: 9px; font-size: 24px; font-weight: 400; }
  .newsletter p { position: absolute; left: 11px; top: 41px; font-size: 15px; text-transform: uppercase; color: #f1d8df; }
  .newsletter p strong { font-weight: 400; color: var(--white); }
  .subscribe-button { position: absolute; left: 437px; top: 17px; width: 146px; height: 38px; border-radius: 8px; background: var(--navy); color: var(--white); font-size: 11px; font-weight: 700; display: flex; align-items: center; justify-content: center; text-decoration: none; }

  .info-zone { position: absolute; left: 0; top: 711px; width: 820px; height: 251px; background: linear-gradient(180deg, #c9d3cf 0%, #aebe9e 40%, #d5dcd0 100%); }
  .section-bar { position: absolute; left: 110px; width: 413px; height: 26px; background: var(--navy); color: var(--white); font-size: 14px; display: flex; align-items: center; justify-content: center; }
  .section-bar::before, .section-bar::after { content: ""; flex: 1; height: 3px; margin: 0 12px; border-top: 1px solid #8a95b5; border-bottom: 1px solid #8a95b5; }
  .about-bar { top: 14px; }
  .events-bar { top: 119px; padding-right: 60px; }
  .about-text { position: absolute; left: 110px; top: 43px; width: 413px; height: 70px; background: rgba(255,255,255,.75); padding: 4px 6px; font-size: 9.3px; line-height: 12px; }
  .about-text::first-letter { font-size: 15px; }
  .about-text a { color: var(--navy); text-decoration: none; }
  .events-arrows { position: absolute; left: 470px; top: 121px; display: flex; gap: 4px; }
  .events-arrows span { width: 22px; height: 22px; border: 1px solid var(--navy); background: var(--navy); display: flex; align-items: center; justify-content: center; }
  .events-arrows span.next { background: var(--white); }
  .event-card { position: absolute; top: 156px; width: 206px; height: 77px; background: var(--white); border: 1px solid #555; display: flex; align-items: center; gap: 8px; padding: 3px; }
  .event-card:nth-of-type(1) { left: 110px; }
  .event-card:nth-of-type(2) { left: 318px; }
  .event-thumb { width: 78px; height: 69px; flex: none; }
  .event-card p { font-size: 9.5px; line-height: 12px; text-transform: uppercase; }
  .ad-slot { position: absolute; left: 533px; top: 14px; width: 170px; height: 218px; background: linear-gradient(180deg, #2d6f9d 0%, #6aa4c8 60%, #e9eef1 80%, #f5f5f5 100%); border: 1px solid #ccc; }

  .site-footer { position: absolute; left: 0; top: 962px; width: 820px; height: 201px; background: var(--footer); }
  .footer-col { position: absolute; top: 16px; }
  .footer-col h4 { font-size: 12px; font-weight: 400; text-transform: uppercase; color: #333; margin-bottom: 10px; }
  .col-social { left: 129px; width: 170px; }
  .social-links { display: flex; gap: 6px; margin-bottom: 25px; }
  .social-links span { width: 25px; height: 25px; border-radius: 50%; background: #555; }
  .social-links span:first-child { background: var(--navy); }
  .post-title { font-size: 9px; color: #555; }
  .post-date { font-size: 6px; color: #999; margin-bottom: 3px; }
  .post-body { font-size: 8px; line-height: 12px; color: #555; margin-bottom: 6px; }
  .read-more { font-family: "Tinos", serif; font-size: 8.5px; color: #333; text-decoration: none; }
  .col-advertise { left: 323px; width: 175px; }
  .ad-links { list-style: none; }
  .ad-links li { font-size: 7px; color: var(--navy); padding: 4px 0 4px 8px; border-bottom: 1px solid #d4d7da; position: relative; }
  .ad-links li::before { content: "»"; position: absolute; left: 0; color: #999; }
  .col-contact { left: 516px; width: 176px; }
  .contact-form .field { display: block; width: 176px; height: 20px; background: var(--white); border: 1px solid #d3d6d9; margin-bottom: 4px; font-family: "Tinos", serif; font-size: 8px; color: #999; padding: 4px 6px; }
  .contact-form .field.message { height: 75px; }
  .contact-form .submit { display: inline-block; background: var(--navy); color: var(--white); font-size: 8px; font-weight: 700; padding: 4px 8px; margin-top: 2px; }

  .bottom-bar { position: absolute; left: 0; top: 1163px; width: 820px; height: 37px; background: var(--bar); color: #ccc; font-size: 7px; }
  .bottom-bar p { position: absolute; left: 129px; top: 14px; }
</style>
</head>
<body>
  <section class="hero" role="img" aria-label="Photograph of ripening grain stalks in a field">
    <h1 class="hero-title">Growing Clean<br>&amp;<br><span class="accent">Full of Health Products</span></h1>
    <div class="slider-dots"><span></span><span></span><span></span></div>
  </section>

  <header class="site-header">
    <a class="brand" href="#"><span class="brand-mark"></span><span class="brand-name">Texas Marsh Reed Conservation League</span></a>
    <nav class="main-nav">
      <a class="is-active" href="#">Home</a>
      <a href="#">About</a>
      <a href="#">Resources</a>
      <a href="#">News Events</a>
      <a href="#">Membership</a>
      <a href="#">Contact</a>
    </nav>
  </header>

  <section class="join-band">
    <h2>ORGANIC PRODUCTS GROWN WITH LOVE</h2>
    <p>When quality matters to you and your customers</p>
    <a class="join-button" href="#">
      <svg width="34" height="22" viewBox="0 0 34 22" aria-hidden="true" fill="#fff">
        <circle cx="8" cy="6" r="3.5"/><path d="M2 20c0-5 3-8 6-8s6 3 6 8z"/>
        <circle cx="17" cy="5" r="4"/><path d="M10 21c0-6 3-9 7-9s7 3 7 9z"/>
        <circle cx="26" cy="6" r="3.5"/><path d="M20 20c0-5 3-8 6-8s6 3 6 8z"/>
      </svg>
      <span>Become<br><b>A Member</b></span>
    </a>
  </section>

  <section class="features">
    <article class="feature"><div class="feature-icon" role="img" aria-label="Line illustration of a cow head"></div><h3>LAUDANTIUM</h3><p>Accusantium doloremque laudantium, totam rem aperiam, eaqipsa quae ab illo inventore veritatis et quasi.</p></article>
    <article class="feature"><div class="feature-icon" role="img" aria-label="Line illustration of a wheat ear"></div><h3>TOTAM REM APERIAM</h3><p>Accusantium doloremque laudantium, totam rem aperiam, eaqipsa quae ab illo inventore veritatis et quasi.</p></article>
    <article class="feature"><div class="feature-icon" role="img" aria-label="Line illustration of a bee beside a honey jar"></div><h3>EAQIPSA QUAE ABILLO</h3><p>Accusantium doloremque laudantium, totam rem aperiam, eaqipsa quae ab illo inventore veritatis et quasi.</p></article>
    <article class="feature"><div class="feature-icon" role="img" aria-label="Line illustration of a basket of produce"></div><h3>INVENTORE VERITATIS</h3><p>Accusantium doloremque laudantium, totam rem aperiam, eaqipsa quae ab illo inventore veritatis et quasi.</p></article>
  </section>

  <section class="newsletter">
    <h2>Need a useful advice from breeder?</h2>
    <p>Subscribe to our newsletter ? <strong>Stay in the know</strong></p>
    <a class="subscribe-button" href="#">SUBSCRIBE NOW</a>
  </section>

  <section class="info-zone" role="img" aria-label="Photograph of a marsh with open water and grassland">
    <h2 class="section-bar about-bar">ABOUT &nbsp;TMRCL</h2>
    <p class="about-text">The Texas Marsh Reed Conservation League, Inc. is an organization of scientists, educators, students, commercial pesticide applicators, administrators, and concerned individuals interested in the management and study of aquatic plants. The membership reflects a diversity of federal, state, and local agencies; universities and colleges around the world... <a href="#">Read more &gt;&gt;</a></p>
    <h2 class="section-bar events-bar">UPCOMING EVENTS</h2>
    <div class="events-arrows">
      <span><svg width="8" height="10" viewBox="0 0 8 10"><path d="M6 1 2 5l4 4" stroke="#fff" stroke-width="2" fill="none"/></svg></span>
      <span class="next"><svg width="8" height="10" viewBox="0 0 8 10"><path d="M2 1l4 4-4 4" stroke="#0e2262" stroke-width="2" fill="none"/></svg></span>
    </div>
    <article class="event-card"><div class="event-thumb" role="img" aria-label="Venue sign for a ranch inn" style="background:#e4e4e4"></div><p>2014 TMRCL Conference<br>October 12-14<br>Bluestem Ranch</p></article>
    <article class="event-card"><div class="event-thumb" role="img" aria-label="Photograph of reeds at a pond edge" style="background:linear-gradient(180deg,#8fb35a,#4f7a33)"></div><p>2014 TMRCL Conference<br>October 12-14<br>Bluestem Ranch</p></article>
    <aside class="ad-slot" role="img" aria-label="Member advertisement showing bottles of an algae treatment product"></aside>
  </section>

  <footer class="site-footer">
    <div class="footer-col col-social">
      <h4>Social Links</h4>
      <div class="social-links"><span aria-label="Social network"></span><span aria-label="Social network"></span><span aria-label="Social network"></span></div>
      <h4>Blogs</h4>
      <p class="post-title">Post Title</p>
      <p class="post-date">Friday, 6th April 2000</p>
      <p class="post-body">Lorem ipsum dolor sit amet, consectetur adipiscing elit. Nunc non diam erat. In fringilla massa ut nisi ullamcorper pellentesque.</p>
      <a class="read-more" href="#">Read More »</a>
    </div>
    <div class="footer-col col-advertise">
      <h4>Advertise With Us</h4>
      <ul class="ad-links">
        <li>Lorem ipsum dolor sit</li><li>Amet consectetur</li><li>Praesent vel sem id</li><li>Curabitur hendrerit est</li><li>Aliquam eget erat nec sapien</li><li>Cras id augue nunc</li><li>In nec justo non</li><li>Vivamus mollis enim ut</li><li>Curabitur hendrerit est</li>
      </ul>
    </div>
    <div class="footer-col col-contact">
      <h4>Contact Us</h4>
      <div class="contact-form">
        <span class="field">Name</span>
        <span class="field">Email</span>
        <span class="field message">Massages</span>
        <span class="submit">SUBMIT</span>
      </div>
    </div>
  </footer>

  <div class="bottom-bar"><p>Copyright © 2014 - All Rights Reserved</p></div>
</body>
</html>
```